We need an attractive business card design that is modern and inviting. We like the blue and yellow (or gold) colors that are displayed with the logo. The business should communicate trust, experience, and integrity.

Target Market(s)

Residential and Commercial

Industry/Entity Type

Business

Contact Information for Business Card

Recessed Lighting
LED Retro Fit
Sign Repair
Alarms and Cameras
Mobile Home Services
24hr service calls

Font styles to use
Serif
Sans Serif

Colors
3176b5
0455a3
fece3e
fbee3e

Requirements
Must have
• Brondle Electric
• Owner: Marcus Tivane
• Licensed and Insured
• TECL #58917
Nice to have
• Exquisite Detail!!
• Over 20 years of experience
Should not have
• Nothing boring or traditional!!!

```html
<!DOCTYPE html>
<html lang="en">
<head>
<meta charset="utf-8">
<title>Brondle Electric – Business Card</title>
<link href="https://fonts.googleapis.com/css2?family=Roboto:wght@400;500;700&display=swap" rel="stylesheet">
<style>
  :root {
    --navy: #163f86;
    --navy-deep: #123777;
    --yellow: #e8ee14;
    --paper: #f4f4f4;
    --backdrop: #e4e4e4;
    --ink: #1d1d1d;
  }
  * { box-sizing: border-box; margin: 0; padding: 0; }
  html, body { width: 1200px; height: 576px; overflow: hidden; }
  body {
    background: var(--backdrop);
    font-family: "Roboto", Arial, sans-serif;
    position: relative;
  }
  .card {
    position: absolute;
    top: 139px;
    width: 484px;
    height: 292px;
    border-radius: 6px;
    overflow: hidden;
  }
  .card-front {
    left: 82px;
    background: linear-gradient(180deg, var(--navy) 0%, var(--navy-deep) 100%);
  }
  .card-back {
    left: 602px;
    width: 480px;
    background: linear-gradient(180deg, #ffffff 0%, var(--paper) 100%);
  }
  .brand-mark {
    position: absolute;
    border-radius: 50%;
  }
  .card-front .brand-mark {
    left: 202px; top: 91px;
    width: 76px; height: 76px;
    border: 6px solid #ffffff;
  }
  .card-front .brand-name {
    position: absolute;
    left: 0; right: 0; top: 172px;
    text-align: center;
    color: #ffffff;
    font-size: 31px;
    font-weight: 400;
    letter-spacing: 1px;
  }
  .wave { position: absolute; left: 0; top: 0; }
  .credentials {
    position: absolute;
    right: 21px; top: 26px;
    text-align: right;
    color: #ffffff;
    font-size: 12.5px;
    line-height: 17px;
  }
  .credentials .chev { color: var(--yellow); margin-left: 5px; }
  .card-back .brand-mark {
    left: 22px; top: 86px;
    width: 64px; height: 64px;
    border: 5px solid var(--navy);
  }
  .card-back .brand-name {
    position: absolute;
    left: 100px; top: 86px;
    color: var(--navy);
    font-size: 30px;
    font-weight: 400;
    line-height: 33px;
    letter-spacing: 0.5px;
  }
  .person { position: absolute; left: 21px; top: 226px; }
  .person-name { color: var(--navy); font-size: 19px; font-weight: 700; }
  .person-role { color: var(--ink); font-size: 12px; margin-top: 2px; }
  .contact {
    position: absolute;
    right: 21px; top: 173px;
    text-align: right;
    color: var(--ink);
    font-size: 13px;
    line-height: 17.5px;
    list-style: none;
  }
  .contact li { display: flex; justify-content: flex-end; align-items: center; gap: 8px; }
  .contact svg { width: 11px; height: 11px; fill: var(--navy); }
  .contact .address { padding-right: 0; margin-top: 3px; line-height: 18px; }
</style>
</head>
<body>
  <section class="card card-front">
    <span class="brand-mark"></span>
    <div class="brand-name">BRONDLE ELECTRIC</div>
  </section>

  <section class="card card-back">
    <svg class="wave" width="480" height="292" viewBox="0 0 480 292">
      <path d="M0 0 H480 V124 C410 120 340 96 270 56 C190 14 70 6 0 22 Z" fill="var(--navy)"/>
      <path d="M0 28 C70 12 190 18 270 60 C340 98 410 122 480 128 V140 C400 136 330 112 262 76 C190 38 80 28 0 46 Z" fill="var(--yellow)"/>
      <path d="M60 38 C140 30 220 36 268 62" stroke="var(--yellow)" stroke-width="2" fill="none"/>
    </svg>

    <div class="credentials">
      <div>Licensed &amp; Insured<span class="chev">«</span></div>
      <div>TECL #58917<span class="chev">«</span></div>
    </div>

    <span class="brand-mark"></span>
    <div class="brand-name">BRONDLE<br>ELECTRIC</div>

    <div class="person">
      <div class="person-name">Marcus Tivane</div>
      <div class="person-role">Managing Director</div>
    </div>

    <ul class="contact">
      <li>+111 222 3333
        <svg viewBox="0 0 11 11"><rect x="2.5" y="0" width="6" height="11" rx="1.2"/><rect x="3.6" y="1.5" width="3.8" height="6.5" fill="#fff"/></svg>
      </li>
      <li>www.yourwebsite.com
        <svg viewBox="0 0 11 11"><path d="M0 4 C0 1 11 1 11 4 V5 H8 V3.5 H3 V5 H0 Z"/><path d="M2 6 H9 L10 10 H1 Z"/></svg>
      </li>
      <li>yourname@yourwebsite.com
        <svg viewBox="0 0 11 11"><rect x="0" y="2" width="11" height="7.5"/><path d="M0.5 2.5 L5.5 6.5 L10.5 2.5" stroke="#fff" stroke-width="1" fill="none"/></svg>
      </li>
      <li class="address">3790 Street No.123<br>Ridgemont California 99999</li>
    </ul>
  </section>
</body>
</html>
```